Book Cover for Young Adult Paranormal Fiction

Looking for a book cover for my forthcoming novel "The Harrowgate Chronicles : Crown of Embers". The story revolves around a senior in high school as he discovers he is an Absorber. Someone able to bond spirits in their own body which grants them unique abilities. In Jory's case, at least at first, his pinky hosts a ghost which grants him strength and speed with that hand. Guided by a secretive teacher he is recruited in a battle against monsters and creatures at night.

One of the first is a "Creeper", a creature that prowls graveyards at night - described as sort of an octopus though made of vines and with dozens of arms - which basically captures Jory, the protagonist, and lowers him over the top of its head.

Even as Jory battles creatures at night, he is sent the journal of Captain Dremmel which traces his own journey after the events in the original "Harrowgate" Novel of Agnes Pellbrook. Through it we learn not all the events of that novel were captured accurately. Even as Dremmel searches for Edmund Harrowgate's brother Tobias, we learn more about the "Crown of Embers".

I've attached my own poor attempt at a cover. Some other ideas to consider is that the "Heart" is actually a physical heart, though at this point would be black and stone like - if you're not interested in the "loving heart" shape.

Other than the author name "Dennis Korvath", I'm open to some different design elements.
Additional Information can be found on my site:
http://thevellumhall.example/

Thank you for your consideration.

```html
<!DOCTYPE html>
<html lang="en">
<head>
<meta charset="utf-8">
<title>The Harrowgate Chronicles : Crown of Embers — Book Cover</title>
<link href="https://fonts.googleapis.com/css2?family=Cinzel:wght@400&family=Mrs+Saint+Delafield&display=swap" rel="stylesheet">
<style>
  :root {
    --backdrop: #e6e6e6;
    --cover-base: #3a1414;
    --blood-deep: #2a0a0c;
    --blood-mid: #6e2a26;
    --flesh-light: #c9a58a;
    --teal-mist: #3f6f7a;
    --heart-dark: #120808;
    --series-red: #c8423a;
    --title-cream: #ecd7b4;
    --author-tan: #b9a48e;
  }
  * { margin: 0; padding: 0; box-sizing: border-box; }
  html, body {
    width: 1200px;
    height: 900px;
    overflow: hidden;
    background: var(--backdrop);
  }
  .book-cover {
    position: absolute;
    left: 320px;
    top: 32px;
    width: 560px;
    height: 840px;
    background: var(--cover-base);
    overflow: hidden;
    box-shadow: 0 2px 10px rgba(0,0,0,0.25);
  }
  .cover-art {
    position: absolute;
    inset: 0;
    background:
      radial-gradient(ellipse 44% 36% at 50% 50%, var(--heart-dark) 0%, var(--heart-dark) 62%, rgba(18,8,8,0) 100%),
      radial-gradient(ellipse 60% 30% at 85% 4%, var(--teal-mist) 0%, rgba(63,111,122,0) 100%),
      radial-gradient(ellipse 70% 35% at 45% 22%, var(--flesh-light) 0%, rgba(201,165,138,0) 100%),
      linear-gradient(180deg, var(--blood-mid) 0%, #5a1e1c 45%, var(--blood-deep) 100%);
  }
  .cover-text {
    position: absolute;
    inset: 0;
    text-align: center;
  }
  .series-name {
    position: absolute;
    top: 322px;
    width: 100%;
    font-family: "Mrs Saint Delafield", cursive;
    font-size: 40px;
    color: var(--series-red);
    line-height: 1;
  }
  .book-title {
    position: absolute;
    top: 392px;
    width: 100%;
    font-family: "Cinzel", serif;
    font-weight: 400;
    color: var(--title-cream);
    line-height: 1;
  }
  .book-title .title-word {
    display: block;
    font-size: 44px;
    letter-spacing: 1px;
  }
  .book-title .title-joiner {
    display: block;
    font-family: "Mrs Saint Delafield", cursive;
    font-size: 34px;
    margin: -4px 0 -6px;
  }
  .author-name {
    position: absolute;
    top: 760px;
    width: 100%;
    font-family: "Cinzel", serif;
    font-size: 30px;
    letter-spacing: 1px;
    color: var(--author-tan);
  }
</style>
</head>
<body>
  <main class="book-cover">
    <div class="cover-art" role="img" aria-label="Textured blood-red backdrop with a dark cracked stone heart at the centre"></div>
    <div class="cover-text">
      <p class="series-name">The Harrowgate Chronicles</p>
      <h1 class="book-title">
        <span class="title-word">Crown</span>
        <span class="title-joiner">of</span>
        <span class="title-word">Embers</span>
      </h1>
      <p class="author-name">Dennis Korvath</p>
    </div>
  </main>
</body>
</html>
```